Home Maintenance Business needs a logo design

I need a logo design for my start up home maintenance (home handyman) business. I will be doing basic home services like painting, yard work, plumbing, electrical, odd jobs, light building (shelving), cleaning, changing light bulbs. No job too big or small. I live in a beach area and I need a logo as well. I want some color. My idea is a beach umbrella with a ladder and tools under it???

Industry/Entity Type

Home Improvement

Contact Information for Business Card

Business name: Maple Hearth Services

Font styles to use
Sans Serif

Requirements
Must have
• Scope of services: painting, gutter cleaning, yard work, plumbing, electrical, odd jobs, cleaning handyman services, no job to small
• email address: maplehearthservices@quillpost.net
• phone: 615-470-2958
Nice to have
• colorful card/I live in a beach community/logo with beachy feel yet explain the business

```html
<!DOCTYPE html>
<html lang="en">
<head>
<meta charset="utf-8">
<title>Maple Hearth Services — Identity</title>
<link rel="stylesheet" href="https://fonts.googleapis.com/css2?family=Montserrat:wght@500;600;700&display=swap">
<style>
  :root {
    --orange: #f26a21;
    --blue: #1f4f8f;
    --ink: #1d3a66;
    --white: #ffffff;
    --stage: #ffffff;
    --line: #e4e4e4;
  }
  * { margin: 0; padding: 0; box-sizing: border-box; }
  html, body { width: 1200px; height: 900px; overflow: hidden; background: var(--stage); }
  body { position: relative; font-family: "Montserrat", Arial, sans-serif; }

  .card {
    position: absolute;
    width: 480px; height: 302px;
    background: var(--white);
    border: 1px solid var(--line);
    overflow: hidden;
  }
  .card--front { left: 29px; top: 53px; }
  .card--display { left: 610px; top: 50px; box-shadow: 0 6px 18px rgba(0,0,0,.12); }

  .card__brand { position: absolute; left: 18px; top: 16px; display: flex; align-items: center; gap: 10px; }
  .card__brand-dot { width: 40px; height: 40px; border-radius: 50%; background: var(--orange); flex: none; }
  .card__brand-name { color: var(--orange); font-weight: 700; font-size: 20px; line-height: 1.05; width: 170px; }

  .card__rule { position: absolute; left: 0; top: 97px; width: 100%; height: 3px; background: var(--orange); }

  .card__name {
    position: absolute; left: 22px; top: 150px;
    color: var(--orange); font-weight: 600; font-size: 17px; letter-spacing: .5px;
  }
  .card__contact { position: absolute; left: 232px; top: 135px; list-style: none; }
  .card__contact li { display: flex; align-items: center; gap: 8px; color: var(--ink); font-weight: 600; margin-bottom: 14px; white-space: nowrap; }
  .card__contact .phone { font-size: 17px; }
  .card__contact .email { font-size: 11px; }
  .icon { width: 20px; height: 20px; flex: none; }

  .card__base {
    position: absolute; left: 0; bottom: 0; width: 100%; height: 52px;
    background: linear-gradient(180deg, var(--blue) 0%, var(--blue) 45%, var(--orange) 100%);
  }

  .logo {
    position: absolute; left: 216px; top: 552px;
    display: flex; align-items: center; gap: 34px;
  }
  .logo__mark { width: 240px; height: 240px; border-radius: 50%; background: var(--orange); flex: none; }
  .logo__name { color: var(--orange); font-weight: 700; font-size: 64px; line-height: 1.1; width: 560px; }
</style>
</head>
<body>

  <section class="card card--front" aria-label="Business card">
    <div class="card__brand">
      <span class="card__brand-dot"></span>
      <span class="card__brand-name">Maple Hearth Services</span>
    </div>
    <div class="card__rule"></div>
    <p class="card__name">DANA WELBROOK</p>
    <ul class="card__contact">
      <li class="phone">
        <svg class="icon" viewBox="0 0 20 20"><circle cx="10" cy="10" r="10" fill="var(--ink)"/><path d="M7 5.5l2 2-1 1.3c.6 1.3 1.7 2.4 3 3l1.3-1 2 2-1.3 1.5c-3.5-.3-6.9-3.7-7.2-7.2z" fill="#fff"/></svg>
        615-470-2958
      </li>
      <li class="email">
        <svg class="icon" viewBox="0 0 20 20"><circle cx="10" cy="10" r="10" fill="var(--ink)"/><rect x="5" y="6.5" width="10" height="7" rx="1" fill="#fff"/><path d="M5.5 7l4.5 3.5L14.5 7" stroke="var(--ink)" stroke-width="1" fill="none"/></svg>
        maplehearthservices@quillpost.net
      </li>
    </ul>
    <div class="card__base" role="img" aria-label="Decorative blue and orange band along the card's lower edge"></div>
  </section>

  <section class="card card--display" aria-label="Business card, second view">
    <div class="card__brand">
      <span class="card__brand-dot"></span>
      <span class="card__brand-name">Maple Hearth Services</span>
    </div>
    <div class="card__rule"></div>
    <p class="card__name">DANA WELBROOK</p>
    <ul class="card__contact">
      <li class="phone">
        <svg class="icon" viewBox="0 0 20 20"><circle cx="10" cy="10" r="10" fill="var(--ink)"/><path d="M7 5.5l2 2-1 1.3c.6 1.3 1.7 2.4 3 3l1.3-1 2 2-1.3 1.5c-3.5-.3-6.9-3.7-7.2-7.2z" fill="#fff"/></svg>
        615-470-2958
      </li>
      <li class="email">
        <svg class="icon" viewBox="0 0 20 20"><circle cx="10" cy="10" r="10" fill="var(--ink)"/><rect x="5" y="6.5" width="10" height="7" rx="1" fill="#fff"/><path d="M5.5 7l4.5 3.5L14.5 7" stroke="var(--ink)" stroke-width="1" fill="none"/></svg>
        maplehearthservices@quillpost.net
      </li>
    </ul>
    <div class="card__base" role="img" aria-label="Decorative blue and orange band along the card's lower edge"></div>
  </section>

  <section class="logo" aria-label="Logo">
    <span class="logo__mark"></span>
    <span class="logo__name">Maple Hearth Services</span>
  </section>

</body>
</html>
```